New design for a hotel booking website

I am looking to re-design my hotel booking website peakstaylodging.net. Please find the specs attached. Delivery in PSD format. Two pages total: (i) homepage and (ii) inner page.
I want the design to be very simple to navigate and have a feel that is related to Banff, Canada. You can keep a similar layout as the current website.
Requirements
1) Homepage
- Booking form above the fold containing the check in & check out dates, # of rooms and the Search button
- Quality image relating to the city of Banff to make it clear what city this is (no slider - I don't want any animation)
- A section for featured hotels (3-5 items)
- A section for links to other sections on the website (currently under "Explore Banff")
- A section for articles and local guides
- A weather widget (either in the header or somewhere else, similar to this one http://clipvanta.com/t/QX7RLPd2K4)
2) Hotel listings page - http://www.peakstaylodging.net/hotels
- Left or right sidebar – must contain the booking form with the same fields as on the homepage
- A section of why to book hotels with us under the booking form
- Each hotel listing should contain the following
Hotel name
Star rating
Short description (same as currently on the website)
Thumbnail
Address
A button to Check Rates
Notes
- I want the design to be user friendly, simple and easy to use
- I want it to be related to Banff. Banff is a resort town in Alberta, Canada with mountains for skiing in the winter and parks and wildlife nature in the summer.
- Delivery format: PSD
- I want the layout to be easily convertible into a responsive design
- Small social media icon to the Chatterly page (with the option to add Vidzo and Quippr in the future)
Some competing website examples:
1) corvelridgeway.com/Places-to-Stay/Hotels-Inns
2) tornivastays.org
Some examples of websites I liked:
1) http://www.quellmont.com/accommodation/hotels/
2) http://www.lodgevanterra.com/
Target Market(s)
Anyone looking to book their stay in Banff, AB, Canada.
Industry/Entity Type
Travel
Number of Pages Required
2 page
Look and feel

```html
<!DOCTYPE html>
<html lang="en">
<head>
<meta charset="utf-8">
<title>Peak Stay Lodging – Compare Prices on Accommodations in Banff</title>
<link rel="stylesheet" href="https://fonts.googleapis.com/css2?family=Oswald:wght@400;500;600&family=Lato:wght@400;700;900&display=swap">
<style>
:root{
  --blue:#2a9be0;
  --blue-dark:#1c7fc0;
  --navy:#0d2a3f;
  --topbar:#4d4d4d;
  --ink:#222;
  --text:#444;
  --muted:#777;
  --panel:#ececec;
  --footer:#242424;
  --gold:#f5b800;
  --white:#fff;
}
*{box-sizing:border-box;margin:0;padding:0}
html,body{width:1200px;height:2799px;overflow:hidden}
body{font-family:"Lato",Arial,sans-serif;color:var(--text);background:var(--white);position:relative}
.wrap{width:1028px;margin:0 auto;position:relative}
a{color:inherit;text-decoration:none}

/* top bar */
.topbar{height:37px;background:var(--topbar);color:#eee;font-size:13px}
.topbar .wrap{display:flex;align-items:center;height:37px}
.topbar .contact{display:flex;gap:30px;align-items:center}
.topbar .contact span{display:flex;align-items:center;gap:8px}
.topbar .social{margin-left:auto;display:flex;height:37px}
.topbar .social i{width:34px;height:37px;border-left:1px solid #666;display:flex;align-items:center;justify-content:center}
.topbar .social i::after{content:"";width:9px;height:9px;border-radius:50%;background:#ddd}

/* header */
.header{height:105px}
.header .wrap{display:flex;align-items:center;height:105px}
.brand-name{font-family:"Oswald",sans-serif;font-weight:600;font-size:40px;color:var(--blue);letter-spacing:-.5px;line-height:1}
.brand-tag{font-family:"Lato",sans-serif;font-size:12.5px;color:var(--blue);letter-spacing:.4px;margin-top:4px}
.weather{margin-left:auto;width:154px;height:54px;background:#d6eaf7;border:1px solid #bcd9ee;display:flex;align-items:center;padding-left:8px;font-size:11.5px;color:#345;line-height:1.25}
.weather .temp{color:var(--blue);font-weight:700}
.weather svg{margin-left:auto;margin-right:6px}

/* nav */
.nav{height:41px;background:var(--blue)}
.nav ul{list-style:none;display:flex;height:41px}
.nav li{font-family:"Lato",sans-serif;font-weight:700;font-size:13.5px;color:var(--white);display:flex;align-items:center;justify-content:center;border-right:1px solid #4eaee8;flex:1}
.nav li:last-child{border-right:none}
.nav li.active{background:var(--blue-dark);flex:0 0 108px}

/* hero */
.hero{height:517px;position:relative;background:linear-gradient(180deg,#1d3a7a 0%,#3a5a9c 35%,#8a7a8c 55%,#c9cdd8 78%,#e5e8ef 100%)}
.hero .wrap{height:517px}
.booking{position:absolute;left:0;top:75px;width:291px;height:382px;background:rgba(42,155,224,.88)}
.booking h2{height:52px;background:var(--navy);color:var(--white);font-family:"Lato",sans-serif;font-weight:700;font-size:21px;display:flex;align-items:center;padding-left:18px;letter-spacing:.3px}
.booking form{padding:10px 16px 0}
.booking label{display:block;color:var(--white);font-size:15px;font-weight:700;margin:6px 0 6px}
.booking .field{height:43px;background:rgba(255,255,255,.22);border:1px solid rgba(255,255,255,.35);color:var(--white);font-size:14px;display:flex;align-items:center;padding:0 12px;margin-bottom:14px}
.booking .field.select{font-style:italic;font-size:12px}
.booking .field svg{margin-left:auto}
.booking .btn{height:44px;background:#000;color:var(--white);font-weight:700;font-size:20px;display:flex;align-items:center;justify-content:center;margin-top:4px}
.hero-copy{position:absolute;right:0;top:235px;text-align:right;color:var(--white);text-shadow:0 2px 4px rgba(0,0,0,.5)}
.hero-copy h1{font-family:"Lato",sans-serif;font-weight:700;font-size:52px;line-height:1}
.hero-copy p{font-family:"Lato",sans-serif;font-size:33px;line-height:1.18;margin-top:14px}

/* section titles */
.sec-title{font-family:"Oswald",sans-serif;font-weight:400;font-size:29px;color:var(--ink);border-left:6px solid var(--blue);padding-left:14px;line-height:40px;letter-spacing:.3px}
.sec-title b{font-weight:600}

/* featured */
.featured{height:528px;padding-top:48px}
.carousel{position:relative;margin-top:40px;display:flex;gap:32px}
.arrow{position:absolute;top:150px}
.arrow.prev{left:-56px}.arrow.next{right:-56px}
.card{width:233px;height:333px;border:1px solid #ddd;position:relative;background:var(--white)}
.card .thumb{height:176px;background:linear-gradient(180deg,#7d9ac4 0%,#b5a48c 60%,#e3e3e6 100%)}
.card .thumb.dusk{background:linear-gradient(180deg,#5a7fc8 0%,#3d5470 55%,#8a8670 100%)}
.card .thumb.snow{background:linear-gradient(180deg,#bfc8d6 0%,#9aa0a8 50%,#eef0f3 100%)}
.price{position:absolute;right:6px;top:136px;width:78px;height:78px;border-radius:50%;background:var(--blue);border:4px solid var(--white);color:var(--white);font-family:"Oswald",sans-serif;font-size:25px;display:flex;align-items:center;justify-content:center}
.price sup{font-size:12px;margin-right:1px}
.card h3{font-family:"Oswald",sans-serif;font-weight:400;font-size:22px;color:var(--ink);line-height:1.25;padding:12px 14px 0}
.stars{color:var(--gold);font-size:20px;padding:2px 14px 0;letter-spacing:1px}
.card p{font-size:12.5px;color:var(--ink);padding:6px 14px 0;line-height:1.55}
.card .corner{position:absolute;right:0;bottom:0}

/* explore + articles */
.explore{height:573px;background:var(--panel);padding-top:42px}
.explore .wrap{display:flex}
.explore-col{width:370px}
.articles-col{flex:1}
.links{list-style:none;margin-top:28px}
.links li{display:flex;align-items:center;height:53px}
.links svg{width:30px;flex:0 0 30px;margin-right:14px}
.links a{font-family:"Oswald",sans-serif;font-size:18px;color:var(--ink);text-decoration:underline}
.article{display:flex;margin-top:22px}
.articles-col .article:first-of-type{margin-top:28px}
.article .pic{width:180px;height:128px;flex:0 0 180px;background:linear-gradient(160deg,#3aa0d6,#1d6fa8 70%,#6fb7de)}
.article .pic.pets{background:linear-gradient(160deg,#8aa0b8,#6d6e70 55%,#b9a27f)}
.article .pic.tub{background:linear-gradient(160deg,#d8c9b4,#e9e2d7 55%,#bcc6cc)}
.article .body{padding-left:28px}
.article h4{font-family:"Oswald",sans-serif;font-weight:400;font-size:18.5px;color:var(--ink);text-transform:uppercase;margin-top:-2px}
.article .meta{color:var(--blue);font-style:italic;font-size:12.5px;margin:6px 0 5px}
.article p{font-size:12.5px;line-height:1.62;color:var(--text)}
.more{color:var(--blue);font-weight:700}

/* why book */
.why{height:366px;padding-top:56px;text-align:center}
.why .sec-title{display:inline-block;font-size:32px}
.features{display:flex;justify-content:space-between;margin-top:34px}
.feature{width:230px}
.feature svg{height:66px}
.feature h5{font-family:"Oswald",sans-serif;font-weight:400;font-size:19px;color:var(--ink);margin:18px 0 8px}
.feature p{font-size:13px;line-height:1.55;color:var(--text)}

/* newsletter */
.newsletter{height:293px;background:linear-gradient(180deg,#1e82bd 0%,#3a9bd2 45%,#5aa8d3 80%,#3e8fc3 100%);text-align:center;color:var(--white);padding-top:56px}
.newsletter h2{font-family:"Oswald",sans-serif;font-weight:400;font-size:40px;letter-spacing:.5px}
.newsletter h2 span{color:#ffd21e}
.newsletter p{font-style:italic;font-size:15px;margin-top:4px}
.subscribe{width:536px;height:48px;margin:34px auto 0;border:2px solid var(--white);border-radius:24px;display:flex;align-items:center;padding-left:20px;font-size:16px}
.subscribe .btn{margin-left:auto;width:176px;height:44px;border-radius:22px;background:#111;color:#ffd21e;font-family:"Oswald",sans-serif;font-size:17px;font-weight:500;display:flex;align-items:center;justify-content:center}

/* footer */
.footer{height:307px;background:var(--footer);color:#ddd;padding-top:38px}
.footer .wrap{display:flex}
.f-about{width:356px}
.f-about .brand-name{color:#bbb;font-size:30px}
.f-about .brand-tag{color:#bbb;font-size:10px}
.f-about p{font-size:13.5px;line-height:1.55;margin-top:18px;color:#eee}
.f-about .read{color:var(--blue);font-weight:700;font-size:13.5px;display:block;margin-top:12px}
.follow{display:flex;align-items:center;gap:18px;margin-top:22px;font-family:"Oswald",sans-serif;font-size:18px;color:#fff}
.follow span{color:var(--blue)}
.follow i{width:18px;height:18px;border-radius:50%;background:#777;display:block}
.f-col h6{font-family:"Oswald",sans-serif;font-weight:400;font-size:18px;color:#fff;margin-bottom:14px}
.f-col h6 span{color:var(--blue)}
.f-links{width:199px}
.f-links ul{list-style:none}
.f-links li{font-size:13px;line-height:25px;color:#eee}
.f-links li::before{content:"";display:inline-block;width:4px;height:4px;border-radius:50%;background:var(--blue);margin-right:12px;vertical-align:middle}
.f-contact{width:275px}
.f-contact .row{display:flex;align-items:center;gap:14px;font-size:13px;line-height:1.5;margin-bottom:18px;color:#eee}
.f-gallery{flex:1}
.gallery{display:grid;grid-template-columns:88px 88px;gap:14px 12px}
.gallery div{height:60px;border:2px solid #ddd}
.g1{background:linear-gradient(160deg,#4b86c8,#7f7765)}
.g2{background:linear-gradient(160deg,#c9a97a,#7a5a44)}
.g3{background:linear-gradient(160deg,#8a5c3a,#d7b98f)}
.g4{background:linear-gradient(160deg,#2e6fc2,#b9c9e3)}
.copyright{position:absolute;left:0;top:2767px;width:1200px;height:32px;background:var(--blue);color:var(--white);font-size:12.5px;display:flex;align-items:center;justify-content:center}
</style>
</head>
<body>

<div class="topbar">
  <div class="wrap">
    <div class="contact">
      <span><svg width="14" height="10" viewBox="0 0 14 10"><rect x=".5" y=".5" width="13" height="9" fill="none" stroke="#eee"/><path d="M.5 .5 7 6 13.5 .5" fill="none" stroke="#eee"/></svg>info@peakstaylodging.net</span>
      <span><svg width="13" height="13" viewBox="0 0 24 24"><path fill="#eee" d="M6.6 10.8a15 15 0 0 0 6.6 6.6l2.2-2.2c.3-.3.7-.4 1-.2 1.1.4 2.3.6 3.6.6.6 0 1 .4 1 1V20c0 .6-.4 1-1 1A17 17 0 0 1 3 4c0-.6.4-1 1-1h3.5c.6 0 1 .4 1 1 0 1.3.2 2.5.6 3.6.1.3 0 .7-.2 1z"/></svg>877-555-0142</span>
    </div>
    <div class="social" aria-label="Social links"><i></i><i></i><i></i><i></i><i></i></div>
  </div>
</div>

<header class="header">
  <div class="wrap">
    <div class="brand">
      <div class="brand-name">PEAK STAY LODGING</div>
      <div class="brand-tag">COMPARE PRICES ON ACCOMMODATIONS IN BANFF</div>
    </div>
    <div class="weather">
      <div><b>VANCOUVER</b><br><span class="temp">0°C</span><br>Mostly Cloudy</div>
      <svg width="56" height="42" viewBox="0 0 56 42"><circle cx="30" cy="16" r="11" fill="#f7c21a"/><ellipse cx="24" cy="30" rx="20" ry="9" fill="#fff"/><ellipse cx="34" cy="26" rx="12" ry="9" fill="#fff"/></svg>
    </div>
  </div>
</header>

<nav class="nav">
  <div class="wrap">
    <ul>
      <li class="active">HOME</li><li>ABOUT US</li><li>BANFF HOTELS</li><li>BANFF RESORTS</li><li>LODGES</li><li>INNS &amp; MOTELS</li><li>CONTACT US</li>
    </ul>
  </div>
</nav>

<section class="hero" role="img" aria-label="Snow-covered mountain resort lodge at dusk with pine trees and lit windows">
  <div class="wrap">
    <div class="booking">
      <h2>QUICK BOOKING TODAY</h2>
      <form>
        <label>CHECK IN DATE:</label>
        <div class="field">06.01.2016<svg width="13" height="12" viewBox="0 0 13 12"><rect x=".5" y="1.5" width="12" height="10" fill="none" stroke="#fff"/><rect x=".5" y="1.5" width="12" height="3" fill="#fff"/></svg></div>
        <label>CHECK OUT DATE:</label>
        <div class="field">08.01.2016<svg width="13" height="12" viewBox="0 0 13 12"><rect x=".5" y="1.5" width="12" height="10" fill="none" stroke="#fff"/><rect x=".5" y="1.5" width="12" height="3" fill="#fff"/></svg></div>
        <label>ROOM TYPE:</label>
        <div class="field select">Room Type<svg width="14" height="9" viewBox="0 0 14 9"><path d="M1 1l6 6 6-6" fill="none" stroke="#fff" stroke-width="2"/></svg></div>
        <div class="btn">SEARCH</div>
      </form>
    </div>
    <div class="hero-copy">
      <h1>Best Selection</h1>
      <p>Choose from over 47 hotels,<br>resorts and inns in Banff</p>
    </div>
  </div>
</section>

<section class="featured">
  <div class="wrap">
    <h2 class="sec-title">FEATURED <b>HOTELS</b></h2>
    <div class="carousel">
      <svg class="arrow prev" width="22" height="50" viewBox="0 0 22 50"><path d="M20 2 3 25l17 23" fill="none" stroke="#222" stroke-width="2"/></svg>
      <svg class="arrow next" width="22" height="50" viewBox="0 0 22 50"><path d="M2 2l17 23L2 48" fill="none" stroke="#222" stroke-width="2"/></svg>
      <article class="card">
        <div class="thumb" role="img" aria-label="Resort lodge in snowy mountains"></div>
        <div class="price"><sup>$</sup>445</div>
        <h3>Alpenrest<br>Springs Resort</h3>
        <div class="stars">★★★★★</div>
        <p>Lorem ipsum dolor sit amet,<br><b>2 Beds, 24/7 Service, more...</b></p>
        <svg class="corner" width="22" height="22" viewBox="0 0 22 22"><path d="M22 0v22H0z" fill="#2a9be0"/><path d="M15 10v8M11 14h8" stroke="#fff" stroke-width="2"/></svg>
      </article>
      <article class="card">
        <div class="thumb dusk" role="img" aria-label="Lodge among pine trees at twilight"></div>
        <div class="price"><sup>$</sup>445</div>
        <h3>Alpenrest<br>Springs Resort</h3>
        <div class="stars">★★★★★</div>
        <p>Lorem ipsum dolor sit amet,<br><b>2 Beds, 24/7 Service, more...</b></p>
        <svg class="corner" width="22" height="22" viewBox="0 0 22 22"><path d="M22 0v22H0z" fill="#2a9be0"/><path d="M15 10v8M11 14h8" stroke="#fff" stroke-width="2"/></svg>
      </article>
      <article class="card">
        <div class="thumb snow" role="img" aria-label="Castle-style hotel in a snowy valley"></div>
        <div class="price"><sup>$</sup>445</div>
        <h3>Alpenrest<br>Springs Resort</h3>
        <div class="stars">★★★★★</div>
        <p>Lorem ipsum dolor sit amet,<br><b>2 Beds, 24/7 Service, more...</b></p>
        <svg class="corner" width="22" height="22" viewBox="0 0 22 22"><path d="M22 0v22H0z" fill="#2a9be0"/><path d="M15 10v8M11 14h8" stroke="#fff" stroke-width="2"/></svg>
      </article>
      <article class="card">
        <div class="thumb" role="img" aria-label="Resort lodge in snowy mountains"></div>
        <div class="price"><sup>$</sup>445</div>
        <h3>Alpenrest<br>Springs Resort</h3>
        <div class="stars">★★★★★</div>
        <p>Lorem ipsum dolor sit amet,<br><b>2 Beds, 24/7 Service, more...</b></p>
        <svg class="corner" width="22" height="22" viewBox="0 0 22 22"><path d="M22 0v22H0z" fill="#2a9be0"/><path d="M15 10v8M11 14h8" stroke="#fff" stroke-width="2"/></svg>
      </article>
    </div>
  </div>
</section>

<section class="explore">
  <div class="wrap">
    <div class="explore-col">
      <h2 class="sec-title">EXPLORE <b>BANFF</b></h2>
      <ul class="links">
        <li><svg viewBox="0 0 30 24" height="24"><path d="M3 20l24-8M8 6l6 6 4-2 4 6" fill="none" stroke="#2a9be0" stroke-width="3"/><circle cx="17" cy="4" r="3" fill="#2a9be0"/></svg><a>Things To Do In Banff</a></li>
        <li><svg viewBox="0 0 30 24" height="24"><path d="M15 1 5 23h20z" fill="#2a9be0"/><rect x="12" y="16" width="6" height="7" fill="#ececec"/></svg><a>Banff Festivals</a></li>
        <li><svg viewBox="0 0 30 24" height="24"><path d="M2 3l26 4M15 5v5" stroke="#2a9be0" stroke-width="2"/><rect x="8" y="10" width="14" height="12" rx="2" fill="#2a9be0"/></svg><a>Experience Summit Skyride</a></li>
        <li><svg viewBox="0 0 30 24" height="24"><path d="M15 1a8 8 0 0 0-8 8c0 6 8 14 8 14s8-8 8-14a8 8 0 0 0-8-8z" fill="#2a9be0"/><circle cx="15" cy="9" r="3" fill="#ececec"/></svg><a>Heli Sightseeing In Banff</a></li>
        <li><svg viewBox="0 0 30 24" height="24"><circle cx="15" cy="3" r="3" fill="#2a9be0"/><path d="M15 7l-3 8 5 8M13 12l-5 3M15 9l5 4M12 15l-4 8" fill="none" stroke="#2a9be0" stroke-width="3"/></svg><a>Hiking In Banff</a></li>
        <li><svg viewBox="0 0 30 24" height="24"><path d="M15 2 3 23h24z" fill="#2a9be0"/><path d="M15 12l-4 11h8z" fill="#ececec"/></svg><a>Camping &amp; Campgrounds</a></li>
        <li><svg viewBox="0 0 30 24" height="24"><rect x="2" y="12" width="26" height="7" fill="#2a9be0"/><rect x="2" y="5" width="4" height="17" fill="#2a9be0"/><rect x="8" y="8" width="8" height="4" fill="#2a9be0"/></svg><a>Hotels Valley Hot Springs</a></li>
        <li><svg viewBox="0 0 30 24" height="24"><rect x="3" y="10" width="8" height="13" fill="#2a9be0"/><rect x="12" y="2" width="9" height="21" fill="#2a9be0"/><rect x="22" y="12" width="6" height="11" fill="#2a9be0"/></svg><a>Nearby Cities</a></li>
      </ul>
    </div>
    <div class="articles-col">
      <h2 class="sec-title">RECENT <b>ARTICLES</b></h2>
      <article class="article">
        <div class="pic" role="img" aria-label="Couple relaxing in a pool"></div>
        <div class="body">
          <h4>Romantic Banff Getaway Hotels</h4>
          <div class="meta">06 Jan 2016 / by Admin</div>
          <p>Banff consistently comes up when people talk about romantic locations in Canada. It's an idyllic village nestled in the Rocky Mountains about two hours drive from Calgary <span class="more">[…]</span></p>
        </div>
      </article>
      <article class="article">
        <div class="pic pets" role="img" aria-label="Dogs beside luggage on a hotel balcony"></div>
        <div class="body">
          <h4>Banff Pet Friendly Hotels</h4>
          <div class="meta">06 Jan 2016 / by Admin</div>
          <p>Banff consistently comes up when people talk about romantic locations in Canada. It's an idyllic village nestled in the Rocky Mountains about two hours drive from Calgary<span class="more">[…]</span></p>
        </div>
      </article>
      <article class="article">
        <div class="pic tub" role="img" aria-label="Couple in a hot tub"></div>
        <div class="body">
          <h4>Banff Hotels With Hot-Tub</h4>
          <div class="meta">06 Jan 2016 / by Admin</div>
          <p>Banff consistently comes up when people talk about romantic locations in Canada. It's an idyllic village nestled in the Rocky Mountains about two hours drive from Calgary <span class="more">[…]</span></p>
        </div>
      </article>
    </div>
  </div>
</section>

<section class="why">
  <div class="wrap">
    <h2 class="sec-title">WHY BOOK WITH <b>PEAK STAY LODGING</b></h2>
    <div class="features">
      <div class="feature">
        <svg viewBox="0 0 50 66" width="50"><path d="M25 2a23 23 0 0 0-23 23c0 17 23 39 23 39s23-22 23-39A23 23 0 0 0 25 2z" fill="#444"/><rect x="13" y="24" width="24" height="7" fill="#fff"/><rect x="13" y="18" width="4" height="17" fill="#fff"/><rect x="19" y="20" width="8" height="4" fill="#fff"/></svg>
        <h5>40,000+ Hotels In Canada</h5>
        <p>Lorem ipsum dolor sit amet, conctet,<br>sed diam nibh eu mod volutpat nibh<br>eu mod. <b>[…]</b></p>
      </div>
      <div class="feature">
        <svg viewBox="0 0 60 66" width="60"><path d="M30 6 52 28 30 56 10 36 12 12z" fill="none" stroke="#444" stroke-width="5" stroke-linejoin="round"/><circle cx="20" cy="20" r="4" fill="#444"/><text x="32" y="42" font-family="Oswald,sans-serif" font-size="18" fill="#444" text-anchor="middle">$</text></svg>
        <h5>Best Price Guarantee</h5>
        <p>Lorem ipsum dolor sit amet, conctet,<br>sed diam nibh eu mod volutpat nibh<br>eu mod. <b>[…]</b></p>
      </div>
      <div class="feature">
        <svg viewBox="0 0 80 66" width="80"><path d="M4 33C16 14 64 14 76 33 64 52 16 52 4 33z" fill="#444"/><circle cx="40" cy="33" r="11" fill="#fff"/><circle cx="40" cy="33" r="6" fill="#444"/><path d="M14 60 66 6" stroke="#fff" stroke-width="8"/><path d="M14 60 66 6" stroke="#444" stroke-width="4"/></svg>
        <h5>No Hidden Charges</h5>
        <p>Lorem ipsum dolor sit amet, conctet,<br>sed diam nibh eu mod volutpat nibh<br>eu mod. <b>[…]</b></p>
      </div>
      <div class="feature">
        <svg viewBox="0 0 60 66" width="60"><path d="M10 50 40 14l14 12-30 36z" fill="none" stroke="#444" stroke-width="4" stroke-linejoin="round"/><circle cx="32" cy="38" r="6" fill="none" stroke="#444" stroke-width="3"/><path d="M4 46l10 14" stroke="#444" stroke-width="4"/></svg>
        <h5>Pay By Cash</h5>
        <p>Lorem ipsum dolor sit amet, conctet,<br>sed diam nibh eu mod volutpat nibh<br>eu mod. <b>[…]</b></p>
      </div>
    </div>
  </div>
</section>

<section class="newsletter" role="img" aria-label="Misty forest lake backdrop in blue tones">
  <h2>NEWSLETTER <span>SIGNUP</span></h2>
  <p>Subscribe to our newsletter to receive news &amp; updates.</p>
  <div class="subscribe">Enter Your Email Id<div class="btn">SUBSCRIBE</div></div>
</section>

<footer class="footer">
  <div class="wrap">
    <div class="f-about">
      <div class="brand-name">PEAK STAY LODGING</div>
      <div class="brand-tag">COMPARE PRICES ON ACCOMMODATIONS IN BANFF</div>
      <p>Lorem ipsum dolor sit amet, consec Lorem ipsum dolor sit ame sec Loret, consec. Lorem ipsum dolor sit ame. Lorem ipsum dolor sit amet, consec Lorem ipsum dolor sit amet, consdolor sit ame sit ait.</p>
      <a class="read">Read More&gt;&gt;</a>
      <div class="follow">Follow <span>Us:</span><i></i><i></i><i></i><i></i></div>
    </div>
    <div class="f-col f-links">
      <h6>Quick <span>Links</span></h6>
      <ul><li>Home</li><li>Banff Hotels</li><li>Banff Resorts</li><li>Lodges</li><li>Inn &amp; Motels</li><li>Contact Us</li></ul>
    </div>
    <div class="f-col f-contact">
      <h6>Contact <span>Details</span></h6>
      <div class="row"><svg width="24" height="24" viewBox="0 0 24 24"><circle cx="12" cy="12" r="12" fill="#fff"/><path d="M12 5a4 4 0 0 0-4 4c0 3 4 8 4 8s4-5 4-8a4 4 0 0 0-4-4z" fill="#242424"/></svg><span>Lorem ipsum, Dollar smit,<br>City Code - 12345</span></div>
      <div class="row"><svg width="24" height="24" viewBox="0 0 24 24"><circle cx="12" cy="12" r="12" fill="#fff"/><path d="M9 7l2 3-1 1a7 7 0 0 0 3 3l1-1 3 2-1 2c-4 0-9-5-9-9z" fill="#242424"/></svg><span>123-456-7890</span></div>
      <div class="row"><svg width="24" height="24" viewBox="0 0 24 24"><circle cx="12" cy="12" r="12" fill="#fff"/><rect x="6" y="8" width="12" height="8" fill="#242424"/><path d="M6 8l6 5 6-5" fill="none" stroke="#fff"/></svg><span>info@companyname.com</span></div>
    </div>
    <div class="f-col f-gallery">
      <h6>Our <span>Gallery</span></h6>
      <div class="gallery">
        <div class="g1" role="img" aria-label="Castle hotel exterior"></div>
        <div class="g2" role="img" aria-label="Hotel bedroom"></div>
        <div class="g3" role="img" aria-label="Hotel room interior"></div>
        <div class="g4" role="img" aria-label="Mountain castle under blue sky"></div>
      </div>
    </div>
  </div>
</footer>
<div class="copyright">Copyright 2015 Peak Stay Lodging. All Rights Reserved.</div>

</body>
</html>
```